political election

Elect Ramiro Duval

for

Pellwick School Board Pl. ?

colors used are red, white, and blue

any other graphics are more than welcome.

need this in fine print at bottom

advertising paid for by candidate

Target Market(s)

voters of the school district

Industry/Entity Type

School

Requirements
Must have
• red white and blue and in fine print advertisement paid for by candidate.
Nice to have
• graphics, art

```html
<!DOCTYPE html>
<html lang="en">
<head>
<meta charset="utf-8">
<title>Elect Ramiro Duval – Pellwick School Board</title>
<link rel="stylesheet" href="https://fonts.googleapis.com/css2?family=Anton&family=Montserrat:ital,wght@0,600;0,700;1,800&display=swap">
<style>
  :root {
    --sign-red: #d6352c;
    --frame-grey: #7c7976;
    --board-light: #e2d9cf;
    --board-dark: #cfc4b8;
    --board-line: rgba(120, 105, 92, 0.12);
    --ink: #161616;
    --campaign-blue: #2a8ac4;
    --rule-blue: #2f6f9f;
    --paper: #ffffff;
  }
  html, body {
    margin: 0;
    padding: 0;
    width: 851px;
    height: 1200px;
    overflow: hidden;
    background: var(--paper);
  }
  .yard-sign {
    display: block;
    width: 851px;
    height: 1200px;
  }
  .sign-edge { fill: var(--sign-red); }
  .sign-frame { fill: var(--frame-grey); }
  .sign-board { fill: url(#boardTone); }
  .sign-lines { fill: url(#boardLines); }
  .rule { fill: var(--rule-blue); }
  .call-to-vote {
    font-family: "Montserrat", sans-serif;
    font-weight: 700;
    font-size: 46px;
    fill: var(--ink);
  }
  .candidate-name {
    font-family: "Anton", sans-serif;
    font-size: 74px;
    fill: var(--ink);
    stroke: var(--paper);
    stroke-width: 5px;
    paint-order: stroke;
    filter: url(#nameShadow);
  }
  .office-for,
  .office-district,
  .office-school,
  .office-seat {
    font-family: "Montserrat", sans-serif;
    font-weight: 600;
  }
  .office-for {
    font-size: 58px;
    font-weight: 700;
    fill: var(--campaign-blue);
  }
  .office-district {
    font-size: 104px;
    fill: var(--ink);
  }
  .office-school {
    font-size: 128px;
    fill: var(--campaign-blue);
    stroke: var(--paper);
    stroke-width: 6px;
    paint-order: stroke;
  }
  .office-seat {
    font-size: 60px;
    fill: var(--ink);
  }
  .disclaimer {
    font-family: "Montserrat", sans-serif;
    font-style: italic;
    font-weight: 800;
    font-size: 19px;
    fill: var(--ink);
  }
</style>
</head>
<body>
<svg class="yard-sign" viewBox="0 0 851 1200" xmlns="http://www.w3.org/2000/svg" aria-labelledby="signTitle">
  <title id="signTitle">Elect Ramiro Duval for Pellwick School Board Pl.</title>
  <defs>
    <linearGradient id="boardTone" x1="0" y1="0" x2="0" y2="1">
      <stop offset="0" stop-color="var(--board-light)"/>
      <stop offset="1" stop-color="var(--board-dark)"/>
    </linearGradient>
    <pattern id="boardLines" width="10" height="9" patternUnits="userSpaceOnUse">
      <rect width="10" height="3" fill="var(--board-line)"/>
    </pattern>
    <filter id="nameShadow" x="-5%" y="-20%" width="110%" height="150%">
      <feDropShadow dx="2" dy="3" stdDeviation="1.5" flood-color="#000" flood-opacity="0.35"/>
    </filter>
  </defs>

  <rect class="sign-edge" x="48" y="71" width="755" height="1078" rx="46"/>
  <rect class="sign-frame" x="68" y="91" width="715" height="1038" rx="28"/>
  <rect class="sign-board" x="72" y="95" width="707" height="1030" rx="25"/>
  <rect class="sign-lines" x="72" y="95" width="707" height="1030" rx="25"/>

  <g class="candidate-block">
    <text class="call-to-vote" x="718" y="238" text-anchor="end">elect</text>
    <rect class="rule" x="72" y="253" width="660" height="5"/>
    <text class="candidate-name" x="140" y="334" textLength="578" lengthAdjust="spacingAndGlyphs">RAMIRO DUVAL</text>
    <rect class="rule" x="72" y="345" width="660" height="5"/>
  </g>

  <g class="office-block">
    <text class="office-for" x="136" y="582" textLength="102" lengthAdjust="spacingAndGlyphs">FOR</text>
    <text class="office-district" x="134" y="674" textLength="584" lengthAdjust="spacingAndGlyphs">PELLWICK</text>
    <text class="office-school" x="134" y="782" textLength="584" lengthAdjust="spacingAndGlyphs">SCHOOL</text>
    <text class="office-seat" x="718" y="840" text-anchor="end" textLength="238" lengthAdjust="spacingAndGlyphs">BOARD PI</text>
  </g>

  <text class="disclaimer" x="425" y="1090" text-anchor="middle" textLength="372" lengthAdjust="spacingAndGlyphs">advertising paid for by candidate</text>
</svg>
</body>
</html>
```